Publisher needs a book cover design for ‘Quiet Harm at the Chalkboard’ book

We need a book cover (front, back, spine) for the 2nd edition of a book entitled ‘Quiet Harm at the Chalkboard’ and subtitled ‘the overlooked layer of pupil welfare, youth security and careful hiring practice’ (inverted commas not to be part of the title and subtitle). The author is Malcolm Pettifer. The publisher is Wendlebury Press. The finished size of the paperback version will be the industry standard 9" x 6". There will be paperback, hardback, and e-book versions. The final number of pages is expected to be in the region 150-180 pages. Text for the back cover is not yet available, but at the bottom of the back cover should be publisher logo (rectangular) on the left and space for the ISBN bar code on the right. The circular logo should be on the spine. The design should be original and not include any stock images that have been created by someone else or may require obtaining a copyright licence to use. Symbols in common use and not copyrighted are probably ok. There are no required images, photographs or symbols except the publisher logo at the left bottom of the back cover and lower spine. Spine lettering should be UK/US style with the top of the writing nearest the front cover. The designer is free to be creative using appropriate diagrams, symbols or abstract designs. Rectangular and circular variants of the publisher logo are attached. Designers are assured that when evaluating designs absolutely no notice whatsoever is taken of a designer's Pixel Guild ranking or status; We are completely output driven, so what matters is the design, not the ranking or status of the designer. In a similar way, designs are not evaluated as 'good' or 'bad' - the winning design will be chosen after review by a design review panel and is not decided arbitrarily by a single person. All submitted designs should be capable of effective copyright assignment.

Target Market(s)

Practitioners, parents, teachers, pupils and academics concerned with child protection, safeguarding and the elimination of emotional abuse of children in the classroom

Font styles to use
Serif
Sans Serif

Requirements
Must have
• • Title, author, edition, subtitle, publisher logo
Nice to have
• • Originality, innovation
Should not have
• • Stock images or anything else requiring additional copyright discussions and negotiations.

```html
<!DOCTYPE html>
<html lang="en">
<head>
<meta charset="utf-8">
<title>Quiet Harm at the Chalkboard — Cover Wrap</title>
<link rel="stylesheet" href="https://fonts.googleapis.com/css2?family=Jost:wght@400;500;800&family=Archivo+Narrow:ital,wght@1,400&display=swap">
<style>
  :root {
    --ink: #2a2a2c;
    --ink-soft: #3a3a3e;
    --stone-light: #f1f0ee;
    --stone-mid: #dcdcde;
    --stone-dark: #c9ccd2;
    --paper: #ffffff;
  }
  * { margin: 0; padding: 0; box-sizing: border-box; }
  html, body { width: 1200px; height: 874px; overflow: hidden; background: var(--stone-light); }
  .cover-wrap { position: relative; width: 1200px; height: 874px; overflow: hidden; font-family: "Jost", sans-serif; color: var(--ink); }
  .stone-surface { position: absolute; inset: 0; }

  .back-blurb { position: absolute; left: 82px; top: 96px; width: 452px; font-family: "Archivo Narrow", sans-serif; font-style: italic; font-size: 11.6px; line-height: 18.4px; color: var(--ink-soft); }
  .back-blurb p + p { margin-top: 18px; }

  .publisher-mark { position: absolute; left: 38px; top: 796px; display: flex; align-items: center; gap: 8px; }
  .publisher-mark .dot { width: 34px; height: 34px; border-radius: 50%; background: var(--ink); }
  .publisher-mark .name { font-size: 16px; font-weight: 500; letter-spacing: 0.04em; color: var(--ink); line-height: 1; }

  .isbn-box { position: absolute; left: 342px; top: 751px; width: 206px; height: 111px; background: var(--paper); }
  .isbn-box span { position: absolute; left: 12px; top: 10px; font-size: 11px; color: var(--ink); }

  .spine-text { position: absolute; left: 611px; top: 44px; transform-origin: 0 0; transform: rotate(90deg); white-space: nowrap; display: flex; align-items: baseline; gap: 14px; }
  .spine-title { font-size: 25px; letter-spacing: 0.02em; }
  .spine-edition { font-size: 13px; font-weight: 800; }
  .spine-author { font-size: 20px; margin-left: 4px; }
  .spine-mark { position: absolute; left: 582px; top: 815px; width: 36px; height: 36px; border-radius: 50%; background: var(--ink); }

  .front-title { position: absolute; left: 648px; top: 82px; font-size: 72px; line-height: 96px; font-weight: 400; letter-spacing: 0.01em; text-transform: uppercase; color: var(--ink); text-shadow: 2px 4px 5px rgba(0,0,0,0.22); }
  .front-subtitle { position: absolute; left: 650px; top: 470px; font-family: "Archivo Narrow", sans-serif; font-style: italic; font-size: 22px; line-height: 30px; color: var(--ink-soft); }
  .front-edition { position: absolute; right: 80px; top: 556px; font-size: 24px; font-weight: 800; color: var(--ink); }
  .front-author { position: absolute; left: 925px; top: 680px; font-size: 54px; line-height: 64px; font-weight: 400; color: var(--ink); text-shadow: 1px 3px 4px rgba(0,0,0,0.18); }
</style>
</head>
<body>
<main class="cover-wrap">
  <svg class="stone-surface" role="img" aria-label="Pale grey veined marble surface crossed by a twisted gold ribbon, spanning back, spine and front" width="1200" height="874" viewBox="0 0 1200 874">
    <defs>
      <linearGradient id="stone" x1="0" y1="0" x2="1" y2="1">
        <stop offset="0" stop-color="#f2f1ef"/>
        <stop offset="0.45" stop-color="#e6e6e8"/>
        <stop offset="0.75" stop-color="#d3d5da"/>
        <stop offset="1" stop-color="#c9ccd2"/>
      </linearGradient>
    </defs>
    <rect width="1200" height="874" fill="url(#stone)"/>
  </svg>

  <section class="back-cover">
    <div class="back-blurb">
      <p>Lorem ipsum dolor sit amet, consectetur adipiscing elit. Pellentesque ac tempor augue, quis pretium ipsum. Vivamus sit amet nulla bibendum urna cursus tincidunt. Morbi lacus enim, aliquam nec dignissim vel, sollicitudin non lorem. Vivamus sem odio, elementum non risus nec, pharetra lobortis enim. Duis in diam a sapien suscipit iaculis in at mi. Maecenas a risus sit amet urna mattis scelerisque ut quis quam. Duis lacinia scelerisque neque eget hendrerit. Praesent quis neque eu leo vulputate tempor vel in turpis. Maecenas varius elementum malesuada. Integer interdum in augue et dignissim.</p>
      <p>Donec id pharetra diam, dapibus ultrices eros. Quisque sodales tortor vel velit gravida, non sollicitudin ipsum varius. Praesent diam dolor, cursus at sodales vel, tincidunt ac elit. Nam vulputate pretium lacus. Orci varius natoque penatibus et magnis dis parturient montes, nascetur ridiculus mus. Nullam et risus est. Nulla aliquam dolor in orci vehicula egestas sit amet sed mi. Maecenas laoreet cursus purus ut aliquet. Cras congue laoreet arcu, sodales porttitor nulla interdum et. Lorem ipsum dolor sit amet, consectetur adipiscing elit. Phasellus efficitur urna nunc, sed cursus tellus rhoncus id. Sed ut facilisis nunc. Fusce odio tortor, feugiat a porta et, rhoncus egestas augue.</p>
    </div>
    <div class="publisher-mark">
      <span class="dot"></span>
      <span class="name">WENDLEBURY PRESS</span>
    </div>
    <div class="isbn-box"><span>ISBN</span></div>
  </section>

  <section class="spine">
    <div class="spine-text">
      <span class="spine-title">QUIET HARM AT THE CHALKBOARD</span>
      <span class="spine-edition">2nd edition</span>
      <span class="spine-author">Malcolm Pettifer</span>
    </div>
    <span class="spine-mark" aria-label="Wendlebury Press"></span>
  </section>

  <section class="front-cover">
    <h1 class="front-title">Quiet<br>Harm at<br>the<br>Chalkboard</h1>
    <p class="front-subtitle">the overlooked layer of<br>pupil welfare, youth security and careful hiring practice</p>
    <p class="front-edition">2nd edition</p>
    <p class="front-author">Malcolm<br>Pettifer</p>
  </section>
</main>
</body>
</html>
```